Business Card Design

Provide project management services to the construction and other industries
Construction services - Civil and Concrete works
Shop Detailing
Structural Modelling
Client side coordination of project teams and consultants
Feasibility Studies for construction projects

Industry/Entity Type

Business

Contact Information for Business Card

Crestline Ops
Darrel Pikett B.Eng (Hons), G.C.Bus.
Director

m: 0412 583 716
e: dpikett@crestlineops.com.au

p: 08 6293 4078
a: 17 Bramblewood Court, Stirling, WA 6021

```html
<!DOCTYPE html>
<html lang="en">
<head>
<meta charset="utf-8">
<title>Crestline Ops – Business Card</title>
<link rel="stylesheet" href="https://fonts.googleapis.com/css2?family=Lato:wght@400;700&display=swap">
<style>
  :root {
    --stage: #000000;
    --card-front: #ffffff;
    --brand-green: #3a7409;
    --ink: #222222;
    --on-green: #ffffff;
  }
  html, body {
    margin: 0;
    padding: 0;
    width: 1200px;
    height: 900px;
    overflow: hidden;
    background: var(--stage);
    font-family: "Lato", Arial, sans-serif;
  }
  .stage {
    position: relative;
    width: 1200px;
    height: 900px;
  }
  .card {
    position: absolute;
    top: 276px;
    width: 477px;
    height: 292px;
    box-sizing: border-box;
  }
  .card--front {
    left: 116px;
    background: var(--card-front);
    color: var(--ink);
    border-radius: 0 50px 0 50px;
  }
  .card--back {
    left: 622px;
    background: var(--brand-green);
    border-radius: 50px 0 50px 0;
  }

  .person {
    position: absolute;
    right: 26px;
    top: 26px;
    text-align: right;
    line-height: 1;
  }
  .person__name {
    font-weight: 700;
    font-size: 18px;
    margin: 0;
  }
  .person__surname { color: var(--brand-green); }
  .person__credentials {
    font-size: 13px;
    font-weight: 700;
  }
  .person__role {
    font-size: 13px;
    margin: 7px 0 0;
  }

  .wordmark {
    position: absolute;
    font-weight: 700;
    letter-spacing: 0.5px;
    white-space: nowrap;
    line-height: 1;
  }
  .card--front .wordmark {
    left: 30px;
    top: 100px;
    font-size: 33px;
    color: var(--ink);
  }
  .card--back .wordmark {
    left: 0;
    right: 0;
    top: 120px;
    text-align: center;
    font-size: 40px;
    color: var(--on-green);
  }

  .contact {
    position: absolute;
    right: 22px;
    top: 173px;
    margin: 0;
    padding: 0;
    list-style: none;
    text-align: right;
    font-size: 13px;
  }
  .contact__item {
    display: flex;
    justify-content: flex-end;
    align-items: center;
    height: 20px;
    gap: 6px;
  }
  .contact__icon {
    width: 10px;
    height: 10px;
    fill: var(--brand-green);
  }
  .address {
    position: absolute;
    right: 22px;
    top: 244px;
    margin: 0;
    font-size: 13px;
    font-style: normal;
  }
</style>
</head>
<body>
<main class="stage">
  <section class="card card--front" aria-label="Card front">
    <div class="person">
      <p class="person__name">Darrel <span class="person__surname">Pikett</span> <span class="person__credentials">B.Eng (Hons), G.C.Bus.</span></p>
      <p class="person__role">Director</p>
    </div>

    <div class="wordmark">CRESTLINE OPS</div>

    <ul class="contact">
      <li class="contact__item">08 6293 4078
        <svg class="contact__icon" viewBox="0 0 10 10" aria-hidden="true"><path d="M2 0.5 L3.6 2.4 L2.8 3.6 Q4 6 6.4 7.2 L7.6 6.4 L9.5 8 L8.2 9.5 Q1 8.5 0.5 1.8 Z"/></svg>
      </li>
      <li class="contact__item">0412 583 716
        <svg class="contact__icon" viewBox="0 0 10 10" aria-hidden="true"><path d="M2 0 H8 V10 H2 Z M3 1.2 V7.6 H7 V1.2 Z M4.4 8.3 H5.6 V9.2 H4.4 Z" fill-rule="evenodd"/></svg>
      </li>
      <li class="contact__item">dpikett@crestlineops.com.au
        <svg class="contact__icon" viewBox="0 0 10 10" aria-hidden="true"><path d="M0 2 H10 V8.5 H0 Z"/><path d="M0.6 2.4 L5 5.6 L9.4 2.4" stroke="#fff" stroke-width="0.9" fill="none"/></svg>
      </li>
    </ul>

    <address class="address">17 Bramblewood Court, Stirling, WA 6021</address>
  </section>

  <section class="card card--back" aria-label="Card back">
    <div class="wordmark">CRESTLINE OPS</div>
  </section>
</main>
</body>
</html>
```